Brellhaven.co.uk Double Sided A4 Folder needs designing
Brellhaven.co.uk needs a folder design
Hi
Thanks you so much for the great designs, we prefer more blue than gold, some of the designs have way to much gold..
Owen
Thank you so much Tobrik ...
nice work @ KorvenDale :)
@Project Holder.
Need your feedback please.
Thanks
KorvenDale
We deal with properties in the mayfair area, you can view the mayfair website to get an idea of the area.
http://www.ostrelwick-area.co.uk/
The title could be 'Your Mayfair Estate Agents'
the look of the folder should have our color blue and gold, ie royal blue and gold design, it should look almost like it is a royal invitation..
examples of some ideas of the design you can get some inspiration below
http://www.prindova.co.uk/royal_blue_and_gold_monogram_wedding_invitation-274819305527183940
http://www.snapvelo.com/photos/inkmarble/5830416297/
http://img.prindovacdn.com/royal_blue_and_gold_floral_envelope_fits_5x7_sizes-p48301927455061273914eg6_325.jpg?t_image1_iid=AB4C1937-2210-4F7E-B913-50DA7E2C18A6&t_text1=Marla%20Quint%0D%0A517%20Ferncroft%20Lane%0D%0AHolvale%2C%20NY%2067890
Our address is as below
Brell Haven
14b Pellam Row
Mayfair
London
W9X 4QF
Dear PH,
Don't you think, an address or any contact info/tagline would be appropriate to be placed on the folder.
Could you give more details on your business (what kind of properties do you deal with/ May be necessary in case of use of images

```html
<!DOCTYPE html>
<html lang="en">
<head>
<meta charset="utf-8">
<title>Brell Haven – A4 Presentation Folder</title>
<link href="https://fonts.googleapis.com/css2?family=Cinzel:wght@400;600;700&family=Lato:wght@400&display=swap" rel="stylesheet">
<style>
  :root {
    --stage: #000000;
    --royal: #1b4fa8;
    --royal-deep: #0d2f78;
    --royal-light: #3f7fd0;
    --gold: #d9ae3c;
    --gold-light: #f3dd8e;
    --gold-deep: #b8892a;
    --cream: #fbf6e6;
    --navy-text: #17306e;
    --white: #ffffff;
  }
  * { margin: 0; padding: 0; box-sizing: border-box; }
  html, body { width: 1200px; height: 980px; overflow: hidden; background: var(--stage); }
  .canvas { position: relative; width: 1200px; height: 980px; }

  .inner-sheet { position: absolute; }
  .inner-sheet svg { display: block; }
  .inner-sheet--back { left: 390px; top: 398px; width: 776px; height: 557px; }
  .inner-sheet--front { left: 313px; top: 132px; width: 821px; height: 636px; }

  .outer-spread { position: absolute; left: 26px; top: 80px; width: 782px; height: 498px; overflow: hidden; }
  .outer-spread > svg { position: absolute; inset: 0; }

  .park-photo {
    position: absolute; left: 0; top: 0; width: 391px; height: 300px;
    background: linear-gradient(180deg, #6f8a3a 0%, #9aa84a 45%, rgba(217,174,60,0) 100%),
                linear-gradient(90deg, #4f6d2a, #a9b45a);
    -webkit-mask: linear-gradient(180deg, #000 60%, transparent 100%);
            mask: linear-gradient(180deg, #000 60%, transparent 100%);
  }
  .city-globe {
    position: absolute; left: 470px; top: 20px; width: 312px; height: 250px;
    border-radius: 50% 0 0 50%;
    background: radial-gradient(ellipse at 45% 55%, #9ad3ef 0%, #4a98d2 45%, rgba(27,79,168,0) 75%);
  }

  .brand-mark { position: absolute; border-radius: 50%; background: var(--royal-deep); border: 3px solid var(--gold-light); }
  .brand-name { position: absolute; font-family: 'Cinzel', serif; font-weight: 600; color: var(--navy-text); text-align: center; letter-spacing: 0.12em; }

  .back-cover .brand-mark { left: 159px; top: 380px; width: 52px; height: 52px; }
  .back-cover .brand-name { left: 0; width: 391px; top: 440px; font-size: 10px; }
  .contact-lines { position: absolute; left: 0; width: 391px; top: 456px; font-family: 'Lato', sans-serif; font-size: 7px; line-height: 10px; color: var(--navy-text); text-align: center; }

  .front-cover .brand-mark { left: 551px; top: 368px; width: 74px; height: 74px; }
  .front-cover .brand-name { left: 391px; width: 391px; top: 452px; font-size: 16px; }

  .cover-title { position: absolute; right: 34px; top: 34px; text-align: right; font-family: 'Cinzel', serif; color: var(--gold-light); line-height: 1; }
  .cover-title .title-small { display: block; font-size: 20px; font-weight: 400; }
  .cover-title .title-large { display: block; font-size: 38px; font-weight: 700; color: var(--gold); }
  .cover-title .title-sub { display: block; font-size: 17px; font-weight: 400; margin-top: 2px; }
</style>
</head>
<body>
<main class="canvas">

  <!-- inner sheet, lower -->
  <section class="inner-sheet inner-sheet--back">
    <svg width="776" height="557" viewBox="0 0 776 557">
      <defs>
        <linearGradient id="backSheet" x1="0" y1="0" x2="0.4" y2="1">
          <stop offset="0" stop-color="#e9d28d"/><stop offset="0.45" stop-color="#ffffff"/><stop offset="1" stop-color="#ffffff"/>
        </linearGradient>
        <linearGradient id="goldPocket" x1="0" y1="0" x2="0" y2="1">
          <stop offset="0" stop-color="#f6e4a4"/><stop offset="1" stop-color="#c9972f"/>
        </linearGradient>
      </defs>
      <rect width="776" height="557" fill="url(#backSheet)"/>
      <path d="M0 370 H380 L405 450 L430 370 H776 V557 H0 Z" fill="url(#goldPocket)"/>
      <g stroke="#fff5d0" stroke-width="1.5" opacity="0.8">
        <path d="M130 400 l20 20 M130 450 l20 -20 M280 400 l-20 20 M280 450 l-20 -20"/>
        <path d="M510 400 l20 20 M510 450 l20 -20 M660 400 l-20 20 M660 450 l-20 -20"/>
      </g>
    </svg>
  </section>

  <!-- inner sheet, upper -->
  <section class="inner-sheet inner-sheet--front">
    <svg width="821" height="636" viewBox="0 0 821 636">
      <defs>
        <linearGradient id="frontSheet" x1="0" y1="0" x2="1" y2="1">
          <stop offset="0" stop-color="#e2c574"/><stop offset="0.5" stop-color="#fbf3d8"/><stop offset="1" stop-color="#ffffff"/>
        </linearGradient>
        <linearGradient id="bluePocket" x1="0" y1="0" x2="0" y2="1">
          <stop offset="0" stop-color="#2a68c0"/><stop offset="1" stop-color="#0d2f78"/>
        </linearGradient>
      </defs>
      <rect x="97" width="724" height="636" fill="url(#frontSheet)"/>
      <circle cx="587" cy="213" r="130" fill="none" stroke="#d8cdb0" stroke-width="14" opacity="0.6"/>
      <path d="M0 451 H378 L400 520 L422 451 H821 V636 H0 Z" fill="url(#bluePocket)"/>
      <g stroke="#8fb6ec" stroke-width="1.5" opacity="0.8">
        <path d="M120 490 l20 20 M120 560 l20 -20 M290 490 l-20 20 M290 560 l-20 -20"/>
        <path d="M520 490 l20 20 M520 560 l20 -20 M690 490 l-20 20 M690 560 l-20 -20"/>
      </g>
    </svg>
  </section>

  <!-- outer spread: back cover + front cover -->
  <section class="outer-spread">
    <svg width="782" height="498" viewBox="0 0 782 498">
      <defs>
        <linearGradient id="spreadGold" x1="0" y1="0" x2="0" y2="1">
          <stop offset="0" stop-color="#f7e6a6"/><stop offset="0.5" stop-color="#e3bb52"/><stop offset="1" stop-color="#c8952c"/>
        </linearGradient>
        <linearGradient id="spreadBlue" x1="0" y1="0" x2="1" y2="1">
          <stop offset="0" stop-color="#0d2f78"/><stop offset="0.5" stop-color="#1b4fa8"/><stop offset="1" stop-color="#3f7fd0"/>
        </linearGradient>
      </defs>
      <rect width="782" height="498" fill="url(#spreadGold)"/>
      <path d="M0 0 H782 V360 C700 330 620 250 470 220 C380 200 330 240 240 270 C150 300 60 290 0 260 Z" fill="url(#spreadBlue)"/>
      <path d="M0 260 C60 290 150 300 240 270 C330 240 380 200 470 220 C620 250 700 330 782 360" fill="none" stroke="#ffffff" stroke-width="5" opacity="0.9"/>
      <path d="M0 275 C70 305 160 312 250 282 C340 252 390 215 480 236 C630 270 710 345 782 376" fill="none" stroke="#ffffff" stroke-width="2" opacity="0.5"/>
      <line x1="391" y1="0" x2="391" y2="498" stroke="#0a224f" stroke-width="1" opacity="0.35"/>
    </svg>

    <div class="back-cover">
      <div class="park-photo" role="img" aria-label="Photograph of a leafy London park with a statue and lawns"></div>
      <div class="brand-mark"></div>
      <p class="brand-name">BRELL HAVEN</p>
      <p class="contact-lines">
        14b Pellam Row, Mayfair, London W9X 4QF<br>
        T: 020 7946 0123 | F: 020 7946 0456<br>
        E: info@brellhaven.co.uk | W: www.brellhaven.co.uk
      </p>
    </div>

    <div class="front-cover">
      <div class="city-globe" role="img" aria-label="Illustration of city towers rising from a globe above water"></div>
      <h1 class="cover-title">
        <span class="title-small">Your</span>
        <span class="title-large">MAYFAIR</span>
        <span class="title-sub">Estate Agents</span>
      </h1>
      <div class="brand-mark"></div>
      <p class="brand-name">BRELL HAVEN</p>
    </div>
  </section>

</main>
</body>
</html>
```